They say laughter is the best medicine

This poster is for a nursing pharmacology class room with 70+students. Size is 24" x36". It needs to be a clean design. Would like vintage advertisement banners and script fonts. Would like a black background with an accent color. Please view pictures on word doc for examples.

```html
<!DOCTYPE html>
<html lang="en">
<head>
<meta charset="utf-8">
<title>They Say Laughter Is the Best Medicine – Nursing Pharmacology Poster</title>
<link rel="stylesheet" href="https://fonts.googleapis.com/css2?family=Pinyon+Script&family=Rye&family=Bebas+Neue&family=Gentium+Book+Plus&display=swap">
<style>
  :root {
    --wall: #e4e4e4;
    --ink: #232323;
    --ink-deep: #1b1b1b;
    --cream: #efe4d8;
    --gold: #c6a266;
    --gold-soft: rgba(198, 162, 102, 0.35);
    --yellow: #f3d57c;
    --text-light: #f1ebe4;
  }
  * { margin: 0; padding: 0; box-sizing: border-box; }
  html, body {
    width: 1200px; height: 960px; overflow: hidden;
    background: var(--wall);
  }
  .poster {
    position: absolute; left: 295px; top: 30px;
    width: 610px; height: 900px;
    background: radial-gradient(ellipse at 50% 45%, #2a2a2a 0%, var(--ink) 60%, var(--ink-deep) 100%);
    color: var(--text-light);
    box-shadow: 0 6px 18px rgba(0,0,0,0.25);
    overflow: hidden;
  }
  .inner-frame {
    position: absolute; inset: 28px;
    border: 1px solid var(--gold-soft);
  }
  .corner-ornament {
    position: absolute; width: 78px; height: 78px;
    background: radial-gradient(circle, var(--gold-soft) 0%, rgba(198,162,102,0) 70%);
  }
  .corner-ornament.tl { left: 30px; top: 30px; }
  .corner-ornament.tr { right: 30px; top: 30px; }
  .corner-ornament.bl { left: 30px; bottom: 30px; }
  .corner-ornament.br { right: 30px; bottom: 30px; }
  .edge-ornament {
    position: absolute; left: 265px; width: 80px; height: 18px;
    background: linear-gradient(90deg, rgba(198,162,102,0), var(--gold-soft), rgba(198,162,102,0));
  }
  .edge-ornament.top { top: 20px; }
  .edge-ornament.bottom { bottom: 20px; }
  .rule {
    position: absolute; left: 170px; width: 273px; height: 1px;
    background: var(--gold);
  }
  .centered {
    position: absolute; left: 0; width: 100%; text-align: center;
  }
  .kicker {
    top: 124px;
    font-family: "Pinyon Script", cursive;
    font-size: 58px; line-height: 1;
    color: var(--yellow);
  }
  .label-flourish {
    position: absolute; left: 245px; width: 120px; height: 22px;
    background: linear-gradient(90deg, rgba(198,162,102,0), rgba(198,162,102,0.55), rgba(198,162,102,0));
    border-radius: 50%;
  }
  .label-flourish.above { top: 200px; }
  .label-flourish.below { top: 356px; }
  .label-frame {
    position: absolute; left: 0; top: 0;
  }
  .label-text {
    top: 262px;
    font-family: "Rye", serif;
    font-size: 23px; line-height: 38px;
    color: var(--ink);
  }
  .subhead {
    top: 392px;
    font-family: "Bebas Neue", sans-serif;
    font-size: 40px; line-height: 1;
    color: var(--cream);
  }
  .subhead-flourish {
    position: absolute; top: 412px; width: 40px; height: 14px;
    background: linear-gradient(90deg, rgba(198,162,102,0), rgba(198,162,102,0.6));
    border-radius: 50%;
  }
  .subhead-flourish.left { left: 183px; }
  .subhead-flourish.right { left: 388px; transform: scaleX(-1); }
  .drug-list {
    top: 458px;
    font-family: "Gentium Book Plus", serif;
    font-size: 26px; line-height: 35.5px;
    color: var(--text-light);
    list-style: none;
  }
  .tagline {
    top: 649px;
    font-family: "Gentium Book Plus", serif;
    font-size: 14px; color: var(--text-light);
  }
  .course-title {
    top: 671px;
    font-family: "Bebas Neue", sans-serif;
    font-size: 36px; line-height: 1;
    color: var(--yellow);
  }
  .instructor {
    top: 713px;
    font-family: "Gentium Book Plus", serif;
    font-size: 15px; line-height: 23px;
    color: var(--text-light);
  }
</style>
</head>
<body>
  <main class="poster">
    <div class="inner-frame"></div>
    <div class="corner-ornament tl" role="img" aria-label="Gold scroll corner flourish"></div>
    <div class="corner-ornament tr" role="img" aria-label="Gold scroll corner flourish"></div>
    <div class="corner-ornament bl" role="img" aria-label="Gold scroll corner flourish"></div>
    <div class="corner-ornament br" role="img" aria-label="Gold scroll corner flourish"></div>
    <div class="edge-ornament top" role="img" aria-label="Gold centre scroll ornament"></div>
    <div class="edge-ornament bottom" role="img" aria-label="Gold centre scroll ornament"></div>

    <div class="rule" style="top:131px"></div>
    <h1 class="centered kicker">They Say</h1>
    <div class="rule" style="top:182px"></div>

    <div class="label-flourish above" role="img" aria-label="Gold filigree crest above the banner"></div>
    <svg class="label-frame" width="610" height="900" viewBox="0 0 610 900" aria-hidden="true">
      <path d="M190 222 H420 Q432 222 438 236 L444 250 Q448 258 448 266 V300 Q448 308 444 316 L438 330 Q432 344 420 344 H190 Q178 344 172 330 L166 316 Q162 308 162 300 V266 Q162 258 166 250 L172 236 Q178 222 190 222 Z"
            fill="none" stroke="var(--gold)" stroke-width="2"/>
      <path d="M196 230 H414 Q424 230 429 242 L435 254 Q438 260 438 268 V298 Q438 306 435 312 L429 324 Q424 336 414 336 H196 Q186 336 181 324 L175 312 Q172 306 172 298 V268 Q172 260 175 254 L181 242 Q186 230 196 230 Z"
            fill="var(--cream)" stroke="var(--gold)" stroke-width="1.5"/>
    </svg>
    <p class="centered label-text">Laughter is the<br>best medicine!</p>
    <div class="label-flourish below" role="img" aria-label="Gold filigree crest below the banner"></div>

    <div class="subhead-flourish left" role="img" aria-label="Small gold scroll"></div>
    <h2 class="centered subhead">Well, We Think</h2>
    <div class="subhead-flourish right" role="img" aria-label="Small gold scroll"></div>
    <div class="rule" style="top:438px"></div>

    <ul class="centered drug-list">
      <li>Acetaminophen, Lorazepam, MSO4</li>
      <li>Furosemide, Nitroglycerin, Haloperidol</li>
      <li>Loperamide, Albuterol, Vancomycin</li>
      <li>Insulin &amp; Oxygen</li>
    </ul>

    <p class="centered tagline">Just might be what you want more in certain situations.</p>
    <h3 class="centered course-title">Nursing Pharmacology Concepts</h3>
    <p class="centered instructor">Rosalind Hartwell, PhD, MSN, RN, CCRN, CPN, CNE<br>Clinical Professor</p>
    <div class="rule" style="top:777px"></div>
  </main>
</body>
</html>
```